Fitness industry business card

Dear Designers,

I'm looking to have a business card designed that will appeal to affluent wealthy clients, I would
To have high end clean cut luxurious understated minimalistic feel to the business cards.

I look forward to the first draft of design ideas. I will send the info that I would like to have on the cards shortly.

Best Wishes
Zlata

```html
<!DOCTYPE html>
<html lang="en">
<head>
<meta charset="utf-8">
<title>Zlata Fit — Business Card</title>
<link rel="stylesheet" href="https://fonts.googleapis.com/css2?family=Open+Sans:wght@300;400;700&display=swap">
<style>
  :root {
    --page-bg: #1d1f21;
    --slate-light: #5b6b73;
    --slate-mid: #3a454c;
    --slate-dark: #1f2529;
    --panel-light: #e4e3e4;
    --panel-mid: #a9a8aa;
    --panel-dark: #8c8b8d;
    --ink-light: #f2f4f5;
    --ink-soft: #c9d1d5;
    --ink-dark: #3b3f42;
    --accent-teal: #8fd3d6;
    --accent-sage: #cfe3c6;
    --accent-coral: #e0675a;
    --rule-light: rgba(255,255,255,0.6);
  }
  * { box-sizing: border-box; margin: 0; padding: 0; }
  html, body {
    width: 1200px; height: 1000px; overflow: hidden;
    background: var(--page-bg);
    font-family: "Open Sans", Arial, sans-serif;
  }
  .canvas { position: relative; width: 1200px; height: 1000px; }

  .card {
    position: absolute; width: 700px; height: 400px; overflow: hidden;
    box-shadow: 0 12px 30px rgba(0,0,0,0.55);
  }

  /* Front */
  .card--front { left: 80px; top: 80px; display: flex; }
  .front__panel {
    position: relative; width: 200px; height: 100%;
    background: radial-gradient(circle at 55% 62%, var(--panel-light) 0%, var(--panel-mid) 45%, var(--panel-dark) 100%);
  }
  .front__body {
    position: relative; flex: 1; height: 100%;
    background: radial-gradient(circle at 45% 60%, var(--slate-light) 0%, var(--slate-mid) 45%, var(--slate-dark) 100%);
  }
  .front__top-rule {
    position: absolute; left: 30px; right: 0; top: 122px;
    height: 1px; background: var(--rule-light);
  }
  .front__name {
    position: absolute; left: 30px; top: 82px;
    color: var(--ink-light); font-size: 25px; line-height: 1;
  }
  .front__name .given { font-weight: 300; }
  .front__name .family { font-weight: 700; }
  .front__role {
    position: absolute; left: 44px; top: 130px;
    color: var(--ink-soft); font-size: 9px; letter-spacing: 4px;
  }
  .contact-list { position: absolute; left: 140px; top: 170px; list-style: none; }
  .contact-list li {
    position: relative; padding-left: 26px; margin-bottom: 16px;
    color: var(--ink-light); font-size: 12px; line-height: 1.35;
  }
  .contact-list .bullet {
    position: absolute; left: 0; top: 10px;
    width: 9px; height: 9px; border-radius: 50%;
  }
  .bullet--teal { background: var(--accent-teal); }
  .bullet--sage { background: var(--accent-sage); }
  .bullet--coral { background: var(--accent-coral); }
  .front__bottom-rule {
    position: absolute; left: 0; width: 60%; bottom: 62px;
    height: 1px; background: rgba(0,0,0,0.35);
  }
  .front__brand {
    position: absolute; left: 22px; bottom: 28px;
    color: var(--ink-dark); font-size: 17px; font-weight: 400; line-height: 1;
  }

  /* Back */
  .card--back {
    left: 420px; top: 520px;
    background: radial-gradient(circle at 42% 45%, var(--slate-light) 0%, var(--slate-mid) 45%, var(--slate-dark) 100%);
  }
  .back__brand {
    position: absolute; left: 0; right: 0; top: 184px;
    text-align: center;
    color: var(--ink-light); font-size: 24px; font-weight: 400; line-height: 1;
  }
</style>
</head>
<body>
<main class="canvas">
  <section class="card card--front" aria-label="Business card, front">
    <div class="front__panel">
      <p class="front__brand">Zlata Fit</p>
    </div>
    <div class="front__body">
      <div class="front__top-rule"></div>
      <h1 class="front__name"><span class="given">Olesya</span><span class="family">Zlata</span></h1>
      <p class="front__role">ENGINEER</p>
      <ul class="contact-list">
        <li><span class="bullet bullet--teal"></span>+41 270 518<br>+41 733 902</li>
        <li><span class="bullet bullet--sage"></span>www.zlatafit.com<br>olesya@zlatafit.com</li>
        <li><span class="bullet bullet--coral"></span>14 Linden Row<br>Harrowgate, HG2 7LM</li>
      </ul>
    </div>
    <div class="front__bottom-rule"></div>
  </section>

  <section class="card card--back" aria-label="Business card, back">
    <p class="back__brand">Zlata Fit</p>
  </section>
</main>
</body>
</html>
```